For Sale Poster Design

We need a beautiful and tropical looking FOR SALE poster for our speed boat.

Poster format need to be 297x420mm / 300dpi
PSD with all layers.

The photos from the boat can be downloaded here: www.korvado.nl/photos.zip

Target Market(s)

Tourists, expats

Requirements
Must have
• The poster need to have the following text:

Speed Boat Sale

This beautiful full glass fiber speedboat (location Lombok, Indonesia) is perfect for tropical conditions: island transfer, diving, wake boarding, fishing, private charters and leisure activities.

The newly bought 2x 200 HP TORUMI 4 Stroke (2013) will give you an enormous power on the water with maximum speed of 40 Knot / 74 Km/hour. This will bring you from Lombok to Bali in just 50 minutes and only few minutes long from the famous tropical Gili islands.

The speedboat also has the comfort of a small cabin with skylight, sun controlled ventilation system, a small bed, a toilet and a fridge. There are 16 seats in the open section of the boat. The boat is equipped with modern brand-new GPS, Sonar and an FM / AM Radio system.

This speedboat was built in 2011 and is meticulously maintained to the highest standard. It comes with a captain and boatman.

Specs:
Overall length: 11 Meter 36 feet.
Built year: 2011, Bali
Engines: 2x 200 HP TORUMI 4 Stroke (Bought 2013)
Capacity: Max. 16 People (Incl. Crew)
Max speed: 40 Knot / 74 Km/hour
GPS / Sonar: Pelcorn RM-42TX
Tankage: 300 Liter
Lighting: LED / Halogen

Price 99.000 USD
Nice to have
• Big FOR SALE banner on the poster

```html
<!DOCTYPE html>
<html lang="en">
<head>
<meta charset="utf-8">
<title>Speed Boat For Sale</title>
<link href="https://fonts.googleapis.com/css2?family=Anton&family=Open+Sans:wght@400;600;700&family=Oswald:wght@400;600&display=swap" rel="stylesheet">
<style>
:root{
  --red:#d3232a;
  --ink:#3b3b3b;
  --muted:#6a6a6a;
  --paper:#ffffff;
  --band:#4a4a4a;
  --band-dark:#3a3a3a;
  --sea:#35c2c4;
  --sand:#e9dcc0;
  --cabin:#e7e2d6;
}
*{margin:0;padding:0;box-sizing:border-box}
html,body{width:849px;height:1200px;overflow:hidden;background:var(--paper)}
.poster{position:relative;width:849px;height:1200px;background:var(--paper);font-family:"Open Sans",Arial,sans-serif;color:var(--ink)}
.hero{position:absolute;left:0;top:0;width:849px;height:320px;
  background:linear-gradient(180deg,#3f8fd4 0%,#8cc4ea 45%,var(--sea) 72%,var(--sand) 100%)}
.headline{position:absolute;top:330px;left:0;width:100%;text-align:center;
  font-family:"Anton",Impact,sans-serif;font-size:80px;line-height:1;color:var(--red);letter-spacing:1px}
.intro{position:absolute;top:428px;left:55px;width:739px;text-align:center;
  font-size:15.5px;line-height:1.4;color:var(--ink);font-weight:700}
.gallery{position:absolute;top:522px;left:0;width:849px;height:215px;display:flex;gap:6px}
.gallery .photo{flex:1;background:linear-gradient(160deg,#fbfaf6 0%,var(--cabin) 55%,#b9b2a1 100%)}
.columns{position:absolute;top:758px;left:60px;width:729px;display:flex;gap:40px}
.columns .col{flex:1;font-size:11.5px;line-height:1.5;color:var(--muted)}
.columns p{margin-bottom:10px}
.columns strong{color:var(--ink)}
.specs{position:absolute;left:0;top:955px;width:849px;height:245px;
  background:linear-gradient(180deg,var(--band) 0%,var(--band-dark) 100%);color:#e8e8e8}
.specs h2{position:absolute;left:38px;top:36px;font-family:"Oswald",sans-serif;font-weight:400;font-size:26px;letter-spacing:1px;color:#fff;line-height:1}
.spec-list{position:absolute;left:250px;top:38px;list-style:none;font-size:12.5px;line-height:1.6}
.spec-list b{color:#fff}
.price{position:absolute;right:50px;top:38px;width:170px;height:170px;border-radius:50%;background:var(--red);
  display:flex;flex-direction:column;align-items:center;justify-content:center;color:#fff;text-align:center}
.price .label{font-family:"Oswald",sans-serif;font-size:22px;line-height:1}
.price .amount{font-family:"Anton",Impact,sans-serif;font-size:40px;line-height:1.1}
.price .amount small{font-size:14px;font-family:"Oswald",sans-serif}
</style>
</head>
<body>
<div class="poster">
  <div class="hero" role="img" aria-label="White speedboat with twin outboard engines cruising on turquoise tropical water, with beach and palm trees"></div>

  <h1 class="headline">SPEED BOAT FOR SALE</h1>
  <p class="intro">This beautiful full glass fiber speedboat (location Lombok, Indonesia) is perfect for tropical conditions: island transfer, diving, wake boarding, fishing, private charters and leisure activities.</p>

  <div class="gallery">
    <div class="photo" role="img" aria-label="Boat interior with cream upholstered seating"></div>
    <div class="photo" role="img" aria-label="Open deck section with rows of cream seats"></div>
  </div>

  <div class="columns">
    <div class="col">
      <p>This beautiful full glass fiber speedboat (location Lombok, Indonesia) is perfect for tropical conditions: island transfer, diving, wake boarding, fishing, private charters and leisure activities.</p>
      <p>The newly bought 2x 200 HP TORUMI 4 Stroke (2013) will give you an enormous power on the water with maximum speed of 40 Knot / 74 Km/hour. This will bring you from Lombok to Bali in just 50 minutes and only few minutes long from the famous tropical Gili islands.</p>
    </div>
    <div class="col">
      <p>The speedboat also has the comfort of a small cabin with skylight, sun controlled ventilation system, a small bed, a toilet and a fridge. There are 16 seats in the open section of the boat. The boat is equipped with modern brand-new GPS, Sonar and an FM / AM Radio system.</p>
      <p><strong>This speedboat was built in 2011 and is meticulously maintained to the highest standard. It comes with a captain and boatman.</strong></p>
    </div>
  </div>

  <section class="specs">
    <h2>SPECIFICATIONS</h2>
    <ul class="spec-list">
      <li><b>Overall length:</b> 11 Meter 36 feet</li>
      <li><b>Built year:</b> 2011, Bali</li>
      <li><b>Engines:</b> 2x 200 HP TORUMI 4 Stroke (Bought 2013)</li>
      <li><b>Capacity:</b> Max. 16 People (Incl. Crew)</li>
      <li><b>Max speed:</b> 40 Knot / 74 Km/hour</li>
      <li><b>GPS / Sonar:</b> Pelcorn RM-42TX</li>
      <li><b>Tankage:</b> 300 Liter</li>
      <li><b>Lighting:</b> LED / Halogen</li>
    </ul>
    <div class="price">
      <span class="label">Sale Price</span>
      <span class="amount">99.000<small>USD</small></span>
    </div>
  </section>
</div>
</body>
</html>
```